Website Front Page Banner Design for High Technology Intellectual Property

Develop Graphical Hero Banner to be used on the main page of Veltrona .com. The banner will promote the availability of Veltrona JESD204C IP (Intellectual Property). Please see attached pdf doc and follow details for Static Banner. We are looking for a Banner that is visually attention grabbing and uses imagery of applications that are enabled by the IP we are promoting (Applications such as 5G Wireless Infrastructure, CT/MRI/Ultrasound medical equipment, Radar / LIDAR / Satellites and High-Speed Test and Measurement equipment for a few examples). It would be good if the banner generally follow our color template of Green, White and Black - but the images of applications can use additional colors. Additonally, to learn more about JESD204 - recommend going to the following sites to understand what this IP is used for and what markets it address - additionally, I am open to answer any questions you may have. Sites: https://www.quarnify-tech.com/blog/high-speed-interface/jesd204c/, https://resources.pendrelo.com/p/what-jesd204c-standard-adcs,
Target Market(s)
Various High Technology Markets such as Defense, Medical, Test and Measurement, Industrial / Robotics, Wireless Communications
Industry/Entity Type
Semiconductor
Look and feel

```html
<!DOCTYPE html>
<html lang="en">
<head>
<meta charset="UTF-8">
<title>JESD204C IP – High-Speed Data Converter Interface</title>
<link href="https://fonts.googleapis.com/css2?family=Poppins:wght@300;400;500;600&display=swap" rel="stylesheet">
<style>
  :root {
    --bg: #000000;
    --green: #13c04a;
    --green-bright: #1fd35a;
    --green-dark: #0b2a14;
    --green-deep: #06140a;
    --white: #ffffff;
    --text-muted: #c9cfcb;
    --icon-bg: #0f2316;
  }
  * { margin: 0; padding: 0; box-sizing: border-box; }
  html, body { width: 1200px; height: 600px; overflow: hidden; background: var(--bg); }
  body { font-family: 'Poppins', sans-serif; color: var(--white); }

  .hero {
    position: relative;
    width: 1200px;
    height: 600px;
    overflow: hidden;
    background: var(--bg);
  }
  .hero-visual {
    position: absolute;
    inset: 0;
    background:
      radial-gradient(ellipse 260px 200px at 1000px 260px, rgba(40,200,90,0.55), transparent 70%),
      radial-gradient(ellipse 520px 340px at 900px 320px, rgba(20,110,50,0.45), transparent 75%),
      radial-gradient(ellipse 420px 260px at 640px 380px, rgba(15,80,35,0.35), transparent 75%),
      radial-gradient(ellipse 220px 160px at 0px 0px, rgba(20,120,40,0.5), transparent 75%),
      linear-gradient(90deg, #000 0%, #000 30%, #03110a 55%, #06200f 100%);
  }
  .content {
    position: absolute;
    left: 84px;
    top: 91px;
    width: 360px;
  }
  .tag {
    display: inline-flex;
    align-items: center;
    gap: 6px;
    height: 25px;
    padding: 0 11px;
    border: 1px solid #1d5a2d;
    border-radius: 13px;
    background: var(--green-deep);
    color: var(--green-bright);
    font-size: 9.5px;
    font-weight: 500;
    letter-spacing: 0.6px;
  }
  .tag-dot { width: 4px; height: 4px; border-radius: 50%; background: var(--green-bright); }
  .title {
    margin-top: 30px;
    font-size: 54px;
    font-weight: 500;
    line-height: 1;
    letter-spacing: 1px;
  }
  .title .accent { color: var(--green-bright); font-weight: 600; }
  .subtitle {
    margin-top: 19px;
    font-size: 16.5px;
    font-weight: 400;
  }
  .description {
    margin-top: 23px;
    width: 360px;
    font-size: 11px;
    font-weight: 300;
    line-height: 16.8px;
    color: var(--text-muted);
  }
  .cta {
    display: inline-flex;
    align-items: center;
    gap: 8px;
    margin-top: 38px;
    height: 44px;
    padding: 0 30px;
    border-radius: 22px;
    background: var(--green);
    color: #03140a;
    font-size: 14px;
    font-weight: 600;
    text-decoration: none;
  }
  .specs {
    position: absolute;
    left: 84px;
    top: 487px;
    display: flex;
    gap: 0;
  }
  .spec { display: flex; align-items: flex-start; gap: 12px; }
  .spec + .spec { margin-left: 27px; }
  .spec-icon {
    width: 30px; height: 30px;
    border-radius: 5px;
    background: var(--icon-bg);
    display: flex; align-items: center; justify-content: center;
    margin-top: 3px;
  }
  .spec-value { font-size: 19px; font-weight: 500; line-height: 1.1; }
  .spec-label {
    margin-top: 5px;
    font-size: 7.5px;
    font-weight: 400;
    letter-spacing: 0.8px;
    color: var(--green-bright);
  }
</style>
</head>
<body>
<section class="hero">
  <div class="hero-visual" role="img" aria-label="Glowing green processor chip on a circuit board with flowing particle data waves"></div>

  <div class="content">
    <span class="tag"><span class="tag-dot"></span>NEW INTELLECTUAL PROPERTY</span>
    <h1 class="title">JESD204C <span class="accent">IP</span></h1>
    <p class="subtitle">HIGH-SPEED DATA CONVERTER INTERFACE</p>
    <p class="description">Accelerate your system's data conversion with the industry-leading JESD204C interface IP. Optimized for high-performance and low-latency, it is the ideal solution for next-generation defense, medical imaging, and 5G wireless networks.</p>
    <a class="cta" href="#">Learn More
      <svg width="13" height="13" viewBox="0 0 12 12" fill="none" stroke="#03140a" stroke-width="1.8" stroke-linecap="round" stroke-linejoin="round"><path d="M2 10 L10 2 M4 2 H10 V8"/></svg>
    </a>
  </div>

  <div class="specs">
    <div class="spec">
      <div class="spec-icon">
        <svg width="14" height="14" viewBox="0 0 24 24" fill="none" stroke="#1fd35a" stroke-width="2" stroke-linejoin="round"><path d="M13 2 L4 14 H12 L11 22 L20 10 H12 Z"/></svg>
      </div>
      <div><div class="spec-value">32 Gbps</div><div class="spec-label">LINE RATE</div></div>
    </div>
    <div class="spec">
      <div class="spec-icon">
        <svg width="14" height="14" viewBox="0 0 24 24" fill="none" stroke="#1fd35a" stroke-width="2"><circle cx="12" cy="5" r="3"/><circle cx="5" cy="19" r="3"/><circle cx="19" cy="19" r="3"/><path d="M12 8 V12 M5 16 V13 H19 V16"/></svg>
      </div>
      <div><div class="spec-value">64B/66B</div><div class="spec-label">ENCODING SCHEME</div></div>
    </div>
    <div class="spec">
      <div class="spec-icon">
        <svg width="14" height="14" viewBox="0 0 24 24" fill="none" stroke="#1fd35a" stroke-width="2" stroke-linecap="round" stroke-linejoin="round"><path d="M2 12 H6 L9 4 L15 20 L18 12 H22"/></svg>
      </div>
      <div><div class="spec-value">FEC</div><div class="spec-label">ERROR CORRECTION</div></div>
    </div>
  </div>
</section>
</body>
</html>
```